Business Card & Stationary
Powder Coating Company
Project: Business Card & Stationary
Business Card & Stationary - Miscellaneous
Creative Brief
Professional
Rutger Vandelow
Owner / Operator
4715 Ave K 1/2
nullemail@brindlecoatfinish.com
www.brindlecoatfinish.com
Should list our services, which include Powder Coating, Ceramic Coating and Abrasive Blasting

```html
<!DOCTYPE html>
<html lang="en">
<head>
<meta charset="utf-8">
<title>Brindlecoat Finish – Business Cards</title>
<link href="https://fonts.googleapis.com/css2?family=Open+Sans:wght@400;800&display=swap" rel="stylesheet">
<style>
  :root {
    --red: #c8102e;
    --red-deep: #a50d25;
    --ink: #231f20;
    --black: #0a0a0a;
    --white: #ffffff;
    --line: #cfcfcf;
  }
  * { box-sizing: border-box; margin: 0; padding: 0; }
  html, body { width: 1200px; height: 713px; overflow: hidden; background: var(--white); }
  body { position: relative; font-family: "Open Sans", Arial, sans-serif; }

  .card {
    position: absolute;
    width: 561px;
    height: 321px;
    overflow: hidden;
  }
  .card--front { left: 29px; top: 29px; background: var(--white); border: 1px solid var(--line); }
  .card--red   { left: 617px; top: 29px; background: var(--red); }
  .card--white { left: 29px; top: 377px; background: var(--white); border: 1px solid var(--line); }
  .card--black { left: 617px; top: 377px; background: var(--black); }

  .brand {
    display: flex;
    align-items: center;
    gap: 12px;
    font-weight: 800;
    font-size: 40px;
    letter-spacing: -0.5px;
    line-height: 1;
    color: var(--red);
  }
  .brand__mark { width: 26px; height: 26px; background: var(--red); flex: none; }
  .card--red .brand { color: var(--white); }
  .card--red .brand__mark { background: var(--white); }

  .card--front .brand { position: absolute; left: 24px; top: 34px; font-size: 36px; }

  .swoosh { position: absolute; left: 0; top: 0; width: 561px; height: 321px; }

  .person { position: absolute; left: 30px; top: 150px; }
  .person__name { font-size: 20px; color: var(--red); font-weight: 400; }
  .person__role { font-size: 13px; color: var(--ink); margin-top: 4px; }

  .contact {
    position: absolute;
    right: 28px;
    top: 232px;
    text-align: right;
    color: var(--white);
    font-size: 12px;
    line-height: 15.5px;
  }

  .back {
    position: absolute;
    inset: 0;
    display: flex;
    flex-direction: column;
    align-items: center;
    padding-top: 92px;
  }
  .services {
    margin-top: 72px;
    text-align: center;
    font-size: 14px;
    line-height: 22px;
  }
  .card--red .services, .card--black .services { color: var(--white); }
  .card--white .services { color: var(--ink); }
</style>
</head>
<body>

  <section class="card card--front">
    <svg class="swoosh" viewBox="0 0 561 321" aria-hidden="true">
      <path d="M0,258 C140,232 290,262 410,208 C470,181 520,160 561,154 L561,321 L0,321 Z" fill="var(--red)"/>
      <path d="M0,250 C140,224 290,254 410,200 C470,173 520,152 561,146" fill="none" stroke="var(--ink)" stroke-width="3"/>
    </svg>
    <div class="brand"><span class="brand__mark"></span>Brindlecoat Finish</div>
    <div class="person">
      <p class="person__name">Rutger Vandelow</p>
      <p class="person__role">Owner / Operator</p>
    </div>
    <address class="contact" style="font-style:normal">
      4715 Ave K 1/2<br>
      Phone: (212) 555-0147 | Fax: (212) 555-0193<br>
      Email: nullemail@brindlecoatfinish.com<br>
      www.brindlecoatfinish.com
    </address>
  </section>

  <section class="card card--red">
    <div class="back">
      <div class="brand"><span class="brand__mark"></span>Brindlecoat Finish</div>
      <p class="services">which include Powder Coating,<br>Ceramic Coating and Abrasive Blasting</p>
    </div>
  </section>

  <section class="card card--white">
    <div class="back">
      <div class="brand"><span class="brand__mark"></span>Brindlecoat Finish</div>
      <p class="services">which include Powder Coating,<br>Ceramic Coating and Abrasive Blasting</p>
    </div>
  </section>

  <section class="card card--black">
    <div class="back">
      <div class="brand"><span class="brand__mark"></span>Brindlecoat Finish</div>
      <p class="services">which include Powder Coating,<br>Ceramic Coating and Abrasive Blasting</p>
    </div>
  </section>

</body>
</html>
```